Harrowgate Construction And Masonry Ltd

Black background

Logo - attached

Services (bullet points)
New Builds
Extensions
Refurbishments
Alterations
Brickwork Specialists

Contact details - 01632 960418 or 0791 5530274

Email address - contact@harrowgateconstructionandmasonry.co.uk

Website - www.harrowgateconstructionandmasonry.co.uk

Facebook logo

```html
<!DOCTYPE html>
<html lang="en">
<head>
<meta charset="utf-8">
<title>Harrowgate Construction And Masonry Ltd – Flyer</title>
<link href="https://fonts.googleapis.com/css2?family=Poppins:wght@300;400;600;700&display=swap" rel="stylesheet">
<style>
:root{
  --stage:#c4c4c4;
  --ink:#060606;
  --wall-light:#2a2a2a;
  --wall-mid:#1a1a1a;
  --green:#3bb463;
  --white:#ffffff;
  --warm-orange:#8a6330;
  --warm-red:#6e3a34;
}
*{margin:0;padding:0;box-sizing:border-box}
html,body{width:1200px;height:2192px;overflow:hidden;background:var(--stage);font-family:"Poppins",sans-serif}
.flyer{position:absolute;left:80px;top:423px;width:1040px;height:1346px;background:var(--ink);overflow:hidden;box-shadow:0 30px 50px rgba(0,0,0,.35)}
.backdrop{position:absolute;left:0;top:0;width:1040px;height:1140px;
  background:
    radial-gradient(ellipse 45% 40% at 85% 10%,rgba(138,99,48,.55),transparent 70%),
    radial-gradient(ellipse 40% 45% at 82% 62%,rgba(110,58,52,.55),transparent 70%),
    radial-gradient(ellipse 45% 35% at 40% 55%,var(--ink),transparent 80%),
    linear-gradient(180deg,var(--wall-light),var(--wall-mid) 70%,var(--ink));}
.arc{position:absolute;left:0;top:0}
.brand{position:absolute;left:85px;top:89px;width:290px}
.brand__mark{width:90px;height:110px;background:var(--green);margin-left:100px}
.brand__name{margin-top:16px;color:var(--white);font-weight:600;font-size:24px;line-height:1.25;letter-spacing:1px;text-transform:uppercase;text-align:center}
.services__title{position:absolute;left:197px;top:505px;color:var(--green);font-weight:600;font-size:60px;line-height:1}
.frame{position:absolute;left:0;top:0}
.services__list{position:absolute;left:0;top:0;list-style:none}
.services__item{position:absolute;left:191px;height:44px;display:flex;align-items:center;color:var(--white);font-size:33px;white-space:nowrap;transform:translateY(-50%)}
.services__item svg{width:22px;height:22px;margin-right:15px}
.contact{position:absolute;left:0;top:0;color:var(--white)}
.contact__row{position:absolute;display:flex;align-items:center;white-space:nowrap;transform:translateY(-50%)}
.contact__phones{left:178px;top:1155px;font-weight:700;font-size:42px}
.contact__phones .sep{color:var(--green);font-weight:400;margin:0 22px}
.contact__phones svg{width:34px;height:34px;margin-right:36px}
.contact__email{left:168px;top:1204px;font-size:27px}
.contact__email svg{width:32px;height:24px;margin-right:22px}
.contact__web{left:228px;top:1253px;font-size:19px}
.contact__web .sep{color:var(--green);margin:0 28px}
.contact__follow{color:var(--green);font-size:14px;display:flex;align-items:center}
.contact__follow .square{display:inline-block;width:16px;height:16px;background:var(--green);margin-left:8px}
</style>
</head>
<body>
<main class="flyer">
  <div class="backdrop" role="img" aria-label="Photograph of a dark broken brick wall with a crane hook lifting a pallet of red bricks on the right"></div>

  <svg class="arc" width="1040" height="1346" viewBox="0 0 1040 1346" aria-hidden="true">
    <path d="M150 380 L490 350 Q820 420 800 820 Q770 1060 520 1130" fill="none" stroke="var(--green)" stroke-width="5" opacity=".35"/>
    <path d="M90 1070 L70 1220" fill="none" stroke="var(--green)" stroke-width="5" opacity=".3"/>
  </svg>

  <header class="brand">
    <div class="brand__mark"></div>
    <p class="brand__name">Harrowgate Construction And Masonry Ltd</p>
  </header>

  <h2 class="services__title">Services</h2>
  <svg class="frame" width="1040" height="1346" viewBox="0 0 1040 1346" aria-hidden="true">
    <path d="M197 569 H595 Q605 569 605 579 V763" fill="none" stroke="var(--green)" stroke-width="2.5"/>
    <path d="M151 705 V884 Q151 894 161 894 H561" fill="none" stroke="var(--green)" stroke-width="2.5"/>
  </svg>
  <ul class="services__list">
    <li class="services__item" style="top:606px"><svg viewBox="0 0 22 22"><path d="M3 20 L10 8 L19 3 L14 12 Z M3 20 L12 14" fill="none" stroke="var(--green)" stroke-width="1.5"/></svg>New Builds</li>
    <li class="services__item" style="top:668px"><svg viewBox="0 0 22 22"><path d="M3 20 L10 8 L19 3 L14 12 Z M3 20 L12 14" fill="none" stroke="var(--green)" stroke-width="1.5"/></svg>Extensions</li>
    <li class="services__item" style="top:728px"><svg viewBox="0 0 22 22"><path d="M3 20 L10 8 L19 3 L14 12 Z M3 20 L12 14" fill="none" stroke="var(--green)" stroke-width="1.5"/></svg>Refurbishments</li>
    <li class="services__item" style="top:788px"><svg viewBox="0 0 22 22"><path d="M3 20 L10 8 L19 3 L14 12 Z M3 20 L12 14" fill="none" stroke="var(--green)" stroke-width="1.5"/></svg>Alterations</li>
    <li class="services__item" style="top:850px"><svg viewBox="0 0 22 22"><path d="M3 20 L10 8 L19 3 L14 12 Z M3 20 L12 14" fill="none" stroke="var(--green)" stroke-width="1.5"/></svg>Brickwork Specialists</li>
  </ul>

  <footer class="contact">
    <div class="contact__row contact__phones">
      <svg viewBox="0 0 34 34"><path d="M9 4 L14 10 L11 14 Q14 20 20 23 L24 20 L30 25 L27 30 Q14 30 5 17 Q3 9 9 4 Z" fill="var(--green)"/><path d="M19 6 Q27 7 28 15 M19 11 Q23 12 23 15" fill="none" stroke="var(--green)" stroke-width="2"/></svg>
      <span>01632 960418</span><span class="sep">|</span><span>0791 5530274</span>
    </div>
    <div class="contact__row contact__email">
      <svg viewBox="0 0 32 24"><rect x="1" y="1" width="30" height="22" fill="var(--green)"/><path d="M1 1 L16 14 L31 1" fill="none" stroke="var(--ink)" stroke-width="2"/></svg>
      <span>contact@harrowgateconstructionandmasonry.co.uk</span>
    </div>
    <div class="contact__row contact__web">
      <span>www.harrowgateconstructionandmasonry.co.uk</span><span class="sep">|</span>
      <span class="contact__follow">Follow us:<span class="square"></span></span>
    </div>
  </footer>
</main>
</body>
</html>
```